Leading the way in online fitness and education requires power house web design

If you need to contact me you can do so via
skype: Travlin

We need a website designed for new company based in Houston Texas called "TravlinFit". We offer web based training and nutrition programs for our members for example we use the same software as these companies: http://marobelka.com/ http://www.liftquorra.com/ i would like my visitors to be captivated by the level of design creativity of the site.

colors to use would be grey, orange and green.
for example i like the green of this site http://www.cartbeam.com/
i will upload my logo files so you can get a feel for shades of grey and orange.

there is a 3d effect filter i would like applied to my logo for use in the web design i have uploaded what that effect looks like.

i will need your designs to be complete with all interior pages which will include Home, Fitness, Nutrition, Fit Lounge, Fit Score, Fit School, Contact Us, Sign up.

fit lounge on my site is the same as pathwick on liftquorra and locker room on marobelka just re branded.

fit school is a research corner for members to learn about health and fitness, we are members of major medical journals on health and fitness and will have all our articles be from the newest research findings.

competitor sites
these sites use same software:
http://marobelka.com/
http://www.liftquorra.com/

these sites are other software.
http://home.sprintmesa.com/software-for-athletes.aspx
http://www.vigordex.com/

here are some websites that i like:
http://www.crestwaveplay.com/
http://www.nub-lantern.com/
http://fimzol.com/
http://www.parqudo.com/
http://www.lortavi.de/fandiloop/
http://brisketmade.com/

i also like the greens in this site that i am uploading

I have been reviewing the designs and would like to update everyone at once I do not want a normal fitness website design style, no testimonials, blog post, bodyfat calculator

my website will be a membership based website. i want the website to sell the main points of my fitness app that my members will have access to look at the comments for my selling points, use those points in the site create designs and graphics to visualize those points.

look at these sites and gain inspiration

http://www.tuvelo.com.pl/#/projekty/case-studies
http://www.quendar.com/en#/home#ld-kpvm-402617-0045
http://www.nub-lantern.com/
http://fimzol.com/
http://www.parqudo.com/

i have a few designers asking me what the selling points are, the website needs to be built around these points

main selling points.

overview

programs utilize the best multi-joint exercises combined with high intensity cardio, to give you a full-body workout, efficiently and effectively. This means you’re burning more calories and building more lean muscle per unit of time than traditional weight training and cardio programs.

When you sign up, you''ll receive a work out and diet plan to fit your goals and fitness level. As you progress through your plan, you can use the personal fitness and meal calendar to record your results. When you sign-up we''ll ask you a series of questions and your workouts will be tailored to your exact needs. That means never having to use a generic diet and exercise plan again.

If you''ve ever tried to lose weight and build muscle and didn''t succeed, we feel your pain. Until now, trying to navigate all the fitness fads and latest trends on your own has been difficult. The best option - hiring a certified personal trainer - may be out of your financial reach. That''s where we come in - we''re personal trainers on a mission to help you reach your fitness goals quickly and for less money than in person training. Best of all, we''re here to help you day or night.

Fitness

Personal Fitness Calendar

Tailored to the member’s schedule and flexible to accommodate any changes to a member’s regular fitness schedule. Track your progress and stay on track with your fitness goals.

Custom Fitness Plan

Based on a member’s current physical condition and goals.

• Step by step exercise instructions
• 3-D video demonstrations of over 600 exercises, including functional and body-weight only movements
• Equipment filter can customize plans to your gym’s equipment package
• Record workouts to track exercise history and progression

Nutrition

Nutritional Assessment

Daily recommended caloric intake (Protein, Carbohydrates and Fats), based on personal profile and daily fitness plan.

Custom Meal Plan

Personalized meal plan based on nutritional assessment.

• Choose number of meals per day
• Add dietary restrictions, food preferences or dislikes
• Database of thousands of ingredients allows for hundreds of thousands of meal combinations
• Include favorite foods by entering custom nutritional information

Weight tracking

Calculate goal weight and track weight-loss or weight-gain progress. You will reach your goals in no time.

Fit Lounge

What is the most important part of any workout or fitness program? Staying motivated. And what better form of motivation than positive encouragement from your peers?

Fit Lounge is fitness focused social network for health-minded individuals looking for a simple and convenient place to track their workout goals and monitor their progress. A unique system of motivation, support and accountability makes setting fitness goals and then keeping up with them easy

Track

Start by setting fitness goals that you want to track. They can be anything from running and jogging to how many hours of sleep you are getting and how many glasses of water you are drinking every day. Other members of the travlinfits community might be tracking the same workout goals as you, so you can always join their groups as well.

Share

Once you start tracking your workout goals, you can share your progress with your friends. Reach a new max on your bench press? Let everyone know. Eclipse the 10 mile mark on your daily run? Spread the word! The communication of encouragement back and forth is a great way to ensure that everyone stays on track with their workout goals.

Achieve

Of course, the point of any workout or fitness program is to achieve the goals you’ve set. And with help from travlinfits workout tracking tools and encouragement from the community, you will achieve your workout goals in no time. When you see a friend has achieved his or her fitness goals, you can send them a virtual “fist bump” as a sign of congratulations. The number of “fist bumps” each user accumulates will be displayed on their profile, providing additional motivation and a healthy dose of competition.

Reason: i dont feel the designs i have received are of the quality i am looking for

check this website out, i know its flash, but i also know you can get creative without flash and have nice effects throughout the site.

http://www.driftlane-hub.com/

I dont want plain jane designs, insert the content i provided into the site and have it explored in a unique way. take as much time on the design as you need as i will keep extending deadline until i find one that is perfect.

as said before don't make the site anything like the competition sites, its only purpose is to sell the memberships using content provided so i need an innovative way to for them to explore that content,

as your designing this site add me on skype so i can detail and help brainstorm ideas my skype id is travlin
you can stray from the color scheme a little or throw it away if you want i just want to see how creative you can get.

Industry/Entity Type

School

Requirements
Nice to have
• if you notice at the bottom of http://marobelka.com/ she has the orange bar with the three short content parts, i like the idea of having a space like that for similar content.

on http://www.vigordex.com/ if you look to the left side of the scrolling icons i like the idea of having icons or animated pictures to point of key benefits.

```html
<!DOCTYPE html>
<html lang="en">
<head>
<meta charset="utf-8">
<title>TravlinFit — Home</title>
<link href="https://fonts.googleapis.com/css2?family=Ubuntu:wght@400;500;700&family=Arimo:wght@400;700&display=swap" rel="stylesheet">
<style>
:root{
  --orange:#e8590c;
  --orange-lt:#f47a1f;
  --green:#5a9e0f;
  --green-lt:#7cbf1e;
  --grey-dk:#3a3a3a;
  --grey:#666;
  --grey-lt:#ececec;
  --paper:#f7f7f7;
  --white:#fff;
}
*{box-sizing:border-box;margin:0;padding:0}
html,body{width:938px;height:1200px;overflow:hidden;background:var(--paper)}
body{position:relative;font-family:"Arimo",Arial,sans-serif;color:var(--grey)}
.abs{position:absolute}
.ubu{font-family:"Ubuntu",Arial,sans-serif}

.top-line{left:0;top:0;width:938px;height:2px;background:var(--green)}
.login-tab{left:708px;top:0;width:124px;height:20px;background:var(--green);color:#fff;font-size:10.5px;text-align:center;line-height:19px;border-radius:0 0 6px 6px}
.brand{left:100px;top:16px;display:flex;align-items:center;gap:10px}
.brand-dot{width:44px;height:44px;border-radius:50%;background:var(--orange)}
.brand-name{font-family:"Ubuntu",sans-serif;font-weight:700;font-size:40px;color:var(--grey-dk);letter-spacing:-1px}
.follow{left:640px;top:50px;font-size:14px;font-style:italic;color:var(--grey-dk);display:flex;align-items:center;gap:6px}
.follow span.dot{width:20px;height:20px;border-radius:50%;display:inline-block}

.nav{left:0;top:74px;width:938px;height:28px;background:linear-gradient(var(--orange-lt),var(--orange))}
.nav-line{left:0;top:102px;width:938px;height:4px;background:var(--green-lt)}
.nav a{position:absolute;top:0;height:28px;line-height:28px;color:#fff;font-family:"Ubuntu",sans-serif;font-weight:500;font-size:10.5px;text-decoration:none;letter-spacing:.4px;transform:translateX(-50%)}
.nav a.active{background:var(--green);padding:0 14px;height:30px;top:-2px;line-height:32px;border-radius:3px 3px 0 0}

.hero-photo{left:92px;top:112px;width:332px;height:296px;background:radial-gradient(ellipse at 45% 45%,#d9b79a,#eee 70%);border-radius:40% 40% 10% 10%}
.hero-title{left:342px;top:154px;font-size:37px;color:var(--orange)}
.hero-sub{left:346px;top:188px;font-size:23px;color:var(--green);font-weight:500}
.hero-text{left:346px;top:216px;width:230px;font-size:9.6px;line-height:13.6px;letter-spacing:.4px;color:var(--grey)}
.hero-text b{color:var(--grey-dk)}
.hero-list{left:414px;top:274px;list-style:none;font-size:13px;color:var(--orange)}
.hero-list li{height:21.5px;position:relative;padding-left:12px}
.hero-list li::before{content:"";position:absolute;left:0;top:6px;width:6px;height:6px;border-radius:50%;background:var(--orange)}
.btn-learn{left:416px;top:354px;width:144px;height:28px;border-radius:14px;background:linear-gradient(var(--orange-lt),var(--orange));color:#fff;font-size:14px;font-weight:500;line-height:28px;padding-left:19px;letter-spacing:.5px}
.btn-learn svg{position:absolute;right:18px;top:5px}

.promo{left:653px;top:124px;width:191px;height:264px;background:var(--green-lt);box-shadow:2px 2px 4px rgba(0,0,0,.2)}
.promo::before{content:"";position:absolute;left:-12px;top:44px;border:12px solid transparent;border-right-color:var(--green-lt);border-left:0}
.promo-item{position:absolute;left:5px;width:178px;height:70px;background:var(--orange);border:2px solid #ff9a4d;padding:7px 6px 0 88px;color:#fff;font-size:9px;line-height:12px}
.promo-item b{display:block}
.promo-thumb{position:absolute;left:9px;top:6px;width:73px;height:54px;border:2px solid #fff}

.rule{left:0;top:410px;width:938px;height:4px;background:var(--orange)}
.section-title{left:109px;top:426px;font-size:16.5px;font-weight:700;color:var(--green)}
.section-title em{font-style:normal;color:var(--orange)}
.search{left:614px;top:414px;width:214px;height:40px;border:3px solid var(--orange);border-top:0;background:#fff;padding:9px 8px}
.search-field{position:absolute;left:10px;top:8px;width:150px;height:22px;border:1px solid #ddd;border-radius:11px 0 0 11px;font-size:9px;color:#aaa;padding:5px 8px}
.search-btn{position:absolute;left:160px;top:8px;width:45px;height:22px;background:var(--orange);color:#fff;font-size:10px;font-weight:700;text-align:center;line-height:22px}

.card{top:482px;width:236px;height:116px;background:linear-gradient(#fff,#ececec);border:1px solid #ddd;border-radius:4px;box-shadow:0 3px 4px rgba(0,0,0,.08)}
.card h3{position:absolute;left:9px;top:8px;font-family:"Ubuntu",sans-serif;font-weight:500;font-size:16.5px;color:var(--grey-dk);width:170px;border-bottom:1px dotted #bbb;padding-bottom:4px}
.card-icon{position:absolute;right:-8px;top:-8px;width:54px;height:54px;border-radius:50%;background:radial-gradient(circle at 40% 35%,var(--orange-lt),var(--orange));border:2px solid #fff;box-shadow:0 1px 3px rgba(0,0,0,.3)}
.card p{position:absolute;left:12px;top:50px;width:212px;font-size:8.8px;line-height:13.6px;text-align:justify}
.card p b{color:var(--grey)}

.mag{left:606px;top:473px;width:228px;height:127px;background:#fff;border:1px solid #ddd}
.mag-cover{position:absolute;left:8px;top:5px;width:111px;height:117px;background:linear-gradient(160deg,#e6e0d8,#c88 60%,#6a8fb0)}
.mag h4{position:absolute;left:128px;top:6px;font-size:10.5px;color:var(--grey-dk);line-height:13px}
.mag ul{position:absolute;left:128px;top:40px;list-style:none;font-size:8.8px;color:var(--grey-dk);line-height:11px}
.mag ul li::before{content:"▸ ";color:var(--orange)}
.mag-sub{position:absolute;left:43px;top:94px;width:175px;height:26px;background:var(--orange);color:#fff;font-size:7.5px;letter-spacing:.5px;line-height:26px;padding-left:12px}
.mag-sub b{position:absolute;left:92px;font-size:11px;letter-spacing:0}

.bar-green{left:101px;top:630px;width:477px;height:26px;border-radius:10px;background:linear-gradient(var(--green-lt),var(--green));color:#fff;font-family:"Ubuntu",sans-serif;font-weight:700;font-size:11.5px;line-height:26px;padding-left:13px;letter-spacing:.2px}
.article{left:102px;width:476px;height:70px}
.article .thumb{position:absolute;left:0;top:0;width:82px;height:68px;border:3px solid #fff;box-shadow:0 0 2px rgba(0,0,0,.3)}
.article h5{position:absolute;left:95px;top:-1px;font-family:"Ubuntu",sans-serif;font-weight:500;font-size:11.5px;color:var(--green)}
.article p{position:absolute;left:95px;top:15px;width:380px;font-size:8.7px;line-height:15px;color:var(--grey)}
.article a{position:absolute;left:95px;top:60px;font-size:8.8px;color:#f39a12;text-decoration:none}

.diet-title{left:614px;top:626px;font-family:"Ubuntu",sans-serif;font-weight:700;font-size:14px;color:var(--grey-dk);letter-spacing:.5px}
.diet-title em{font-style:normal;color:var(--orange)}
.video{left:614px;top:650px;width:224px;height:195px;background:#fff;border:1px solid #ddd;box-shadow:0 1px 3px rgba(0,0,0,.1)}
.video-frame{position:absolute;left:6px;top:8px;width:210px;height:158px;background:linear-gradient(#8a5b3a,#b57a48 55%,#6e3f22)}
.play-label{position:absolute;left:66px;top:66px;width:84px;height:28px;border:2px solid rgba(255,255,255,.6);border-radius:4px;color:rgba(255,255,255,.7);font-size:18px;font-weight:700;text-align:center;line-height:24px;letter-spacing:3px}
.controls{position:absolute;left:4px;top:174px;width:216px;height:14px}

.steps{left:106px;top:878px;width:720px;height:60px;border:3px solid var(--green-lt);background:linear-gradient(90deg,#fff 0%,#f2f2f2 75%,var(--green-lt) 90%)}
.step{position:absolute;top:10px;display:flex;align-items:center;gap:10px}
.step-num{width:33px;height:33px;border-radius:50%;background:radial-gradient(circle at 40% 35%,#8fd22f,var(--green));color:#fff;font-family:"Ubuntu",sans-serif;font-size:20px;text-align:center;line-height:33px;border:2px solid #fff;box-shadow:0 1px 2px rgba(0,0,0,.3)}
.step-txt{font-family:"Ubuntu",sans-serif;font-weight:500;font-size:11.8px;line-height:16px;color:var(--orange)}
.btn-start{left:576px;top:13px;width:126px;height:28px;border-radius:14px;background:linear-gradient(#ff8a2a,var(--orange));border:2px solid #fff;box-shadow:0 1px 3px rgba(0,0,0,.3);color:#fff;font-family:"Ubuntu",sans-serif;font-weight:700;font-size:14px;text-align:center;line-height:24px}

.foot-band{left:0;top:952px;width:938px;height:34px;background:var(--orange)}
.crumb{left:132px;top:958px;display:flex;align-items:center;gap:10px;font-size:9.5px;color:#fff}
.crumb-home{width:30px;height:20px;background:#fff;clip-path:polygon(0 0,80% 0,100% 50%,80% 100%,0 100%)}
.foot-area{left:0;top:986px;width:938px;height:190px;background:var(--grey-lt)}
.couple{left:704px;top:960px;width:148px;height:240px;background:linear-gradient(#d9a887,#333 55%,#222);border-radius:40% 40% 0 0}
.col{top:1008px;width:188px}
.col h6{display:flex;align-items:center;gap:5px;font-family:"Ubuntu",sans-serif;font-weight:700;font-size:15px;font-variant:small-caps;color:var(--grey-dk);letter-spacing:.5px}
.col h6 i{width:12px;height:12px;border-radius:50%;background:var(--orange);display:inline-block}
.col h6 em{font-style:normal;color:var(--orange)}
.col p{margin-top:14px;font-size:8.9px;line-height:13.6px;text-align:justify;color:#333}
.foot-bottom{left:0;top:1176px;width:938px;height:24px;background:#dcdcdc}
.foot-icons{left:124px;top:1180px;display:flex;gap:6px}
.foot-icons span{width:16px;height:16px;border-radius:50%}
.copy{left:284px;top:1182px;font-size:9.6px;color:#333}
</style>
</head>
<body>
<div class="abs top-line"></div>
<div class="abs login-tab">Login / Register</div>

<div class="abs brand"><span class="brand-dot"></span><span class="brand-name">TravlinFit</span></div>
<div class="abs follow">Follow us on
  <span class="dot" style="background:#3fb5e8"></span>
  <span class="dot" style="background:#f07c1a"></span>
  <span class="dot" style="background:#2d4f9e"></span>
  <span class="dot" style="background:#c9302c"></span>
</div>

<nav class="abs nav">
  <a class="active" style="left:147px">HOME</a>
  <a style="left:237px">FITNESS</a>
  <a style="left:338px">NUTRITION</a>
  <a style="left:450px">FIT LOUNGE</a>
  <a style="left:557px">FIT SCORE</a>
  <a style="left:663px">FIT SCHOOL</a>
  <a style="left:776px">CONTACT US</a>
</nav>
<div class="abs nav-line"></div>

<div class="abs hero-photo" role="img" aria-label="Woman in sports top sitting on the floor in a stretching pose"></div>
<div class="abs hero-title ubu">Get in Shape !</div>
<div class="abs hero-sub ubu">Stay Fit</div>
<p class="abs hero-text"><b>Welcome to Marobelka.com!</b> You have officially taken the first step towards a healthier, sexier you! Being a model,</p>
<ul class="abs hero-list ubu">
  <li>Weight loss</li><li>Gain Strenght</li><li>Fitness</li>
</ul>
<div class="abs btn-learn ubu">Learn More
  <svg width="18" height="18" viewBox="0 0 18 18"><circle cx="9" cy="9" r="8" fill="#fff"/><path d="M7 5l5 4-5 4z" fill="#e8590c"/></svg>
</div>

<aside class="abs promo">
  <div class="promo-item" style="top:14px"><div class="promo-thumb" role="img" aria-label="Woman doing floor crunches" style="background:linear-gradient(#c9b8a6,#556)"></div><b>Have you</b>Cleansed Yet?! Need some help with shedding</div>
  <div class="promo-item" style="top:94px"><div class="promo-thumb" role="img" aria-label="Measuring tape around a waist" style="background:linear-gradient(#e8c2a6,#222)"></div><b>Have you</b>Cleansed Yet?! Need some help with shedding</div>
  <div class="promo-item" style="top:178px"><div class="promo-thumb" role="img" aria-label="Couple running on a beach" style="background:linear-gradient(#9cc3e6,#e2d6bf)"></div><b>Have you</b>Cleansed Yet?! Need some help with shedding</div>
</aside>

<div class="abs rule"></div>
<h2 class="abs section-title ubu">LIFTQUORRA: THE DO IT <em>YOURSELF WORKOUT AND DIET PLAN</em></h2>
<div class="abs search"><div class="search-field">Search Here..........</div><div class="search-btn">Search</div></div>

<div class="abs card" style="left:94px"><h3>Transform your Body</h3><span class="card-icon"></span>
  <p><b>1001+ Fitness Articles, 800+ Exercise Videos, 600+ Entrees &amp; Recipes,</b> Custom Workout Plans, Lean Muscle Meal Plans for maximum results in minimal time.</p></div>
<div class="abs card" style="left:349px"><h3>Personal Meal Plans</h3><span class="card-icon"></span>
  <p><b>1001+ Fitness Articles, 800+ Exercise Videos, 600+ Entrees &amp; Recipes,</b> Custom Workout Plans, Lean Muscle Meal Plans for maximum results in minimal time.</p></div>

<div class="abs mag">
  <div class="mag-cover" role="img" aria-label="Running magazine cover with two women runners"></div>
  <h4>GET HOT ISSUES<br>ONLY $12 / YEAR</h4>
  <ul><li>Give a Gift</li><li style="margin-top:5px">Subscribe</li><li>Renew</li></ul>
  <div class="mag-sub">CLICK HERE TO <b>SUBSCRIBE</b></div>
</div>

<div class="abs bar-green">WORKOUT AND MEAL PLANS BUILT FOR YOU!</div>
<div class="abs article" style="top:678px">
  <div class="thumb" role="img" aria-label="Woman training with a cable machine in a gym" style="background:linear-gradient(135deg,#6b8fb5,#cfe0ef)"></div>
  <h5>Lean Muscle and Fat Loss</h5>
  <p>In Lorem ipsum dolor sit amet, consectetuer adipiscing elit. In gravida hendrerit tortor. Morbi non nulla. Maecenas aliquet ligula eget nibh. Cras nec velit et nisl molestie ullamcorper. In Lorem ipsum dolor sit amet, consectetuer adipiscing elit.</p>
  <a>Continue reading ›</a>
</div>
<div class="abs article" style="top:770px">
  <div class="thumb" role="img" aria-label="Woman doing sit-ups at home" style="background:linear-gradient(135deg,#d9d0c4,#c0473e)"></div>
  <h5>Personal Fitness Training at Home</h5>
  <p>In Lorem ipsum dolor sit amet, consectetuer adipiscing elit. In gravida hendrerit tortor. Morbi non nulla. Maecenas aliquet ligula eget nibh. Cras nec velit et nisl molestie ullamcorper. In Lorem ipsum dolor sit amet, consectetuer adipiscing elit.</p>
  <a>Continue reading ›</a>
</div>

<div class="abs diet-title"><em>Coustom</em> Diet Plan</div>
<div class="abs video">
  <div class="video-frame" role="img" aria-label="Women doing a yoga stretch on mats in a studio"><div class="play-label">PLAY</div></div>
  <svg class="controls" viewBox="0 0 216 14">
    <path d="M2 2l8 5-8 5z" fill="#333"/>
    <rect x="18" y="6" width="160" height="3" rx="1.5" fill="#ccc"/>
    <circle cx="110" cy="7.5" r="3.5" fill="#333"/>
    <rect x="196" y="2" width="16" height="10" fill="#ddd" stroke="#aaa"/>
  </svg>
</div>

<div class="abs steps">
  <svg class="abs" style="left:0;top:0" width="714" height="54">
    <path d="M186 0l40 27-40 27M410 0l40 27-40 27M600 0l40 27-40 27" fill="none" stroke="#aaa" stroke-width="1"/>
  </svg>
  <div class="step" style="left:26px"><span class="step-num">1</span><span class="step-txt">Write down<br>your goals.</span></div>
  <div class="step" style="left:207px"><span class="step-num">2</span><span class="step-txt">Update your<br>progress daily.</span></div>
  <div class="step" style="left:398px"><span class="step-num">3</span><span class="step-txt">Celebrate your<br>achievements</span></div>
  <div class="abs btn-start">START NOW!</div>
</div>

<div class="abs foot-band"></div>
<div class="abs crumb"><span class="crumb-home"></span>Home</div>
<div class="abs foot-area"></div>

<div class="abs col" style="left:99px"><h6><i></i><span><em>Slim</em> Down</span></h6>
  <p><b>This is not a diet - or some "lose weight fast" gimmick...</b> Instead, it's a simple way to make weight loss a natural part of the life you already live. And guess what? It's fun! You don't have to give up the foods you love or even join a gym. It's about balancing calories in tiny</p></div>
<div class="abs col" style="left:305px"><h6><i></i><span><em>Get</em> Fit</span></h6>
  <p><b>This is not a diet - or some "lose weight fast" gimmick...</b> Instead, it's a simple way to make weight loss a natural part of the life you already live. And guess what? It's fun! You don't have to give up the foods you love or even join a gym. It's about balancing calories in tiny</p></div>
<div class="abs col" style="left:508px"><h6><i></i><span><em>Be</em> Sexy</span></h6>
  <p><b>This is not a diet - or some "lose weight fast" gimmick...</b> Instead, it's a simple way to make weight loss a natural part of the life you already live. And guess what? It's fun! You don't have to give up the foods you love or even join a gym. It's about balancing calories in tiny</p></div>

<div class="abs foot-bottom"></div>
<div class="abs couple" role="img" aria-label="Fit man and woman standing together holding dumbbells"></div>
<div class="abs foot-icons">
  <span style="background:#3fb5e8"></span><span style="background:#f07c1a"></span><span style="background:#2d4f9e"></span><span style="background:#c9302c"></span>
</div>
<div class="abs copy">Copyright © 2011 - Travlin Fit Personal Traning - All rights reserved. Terms and Privacy Policy</div>
</body>
</html>
```